Schriftdesign für Shop-Header Bild (Schmuckhandel) / Online-Marketing Material
Zielgruppe
Wir verkaufen Schmuck im Onlineshop mit Herz
Aufgabenstellung
Wir benötigen den vorgegebenen Text in schöner Form, Farbe und Größe harmonisch eingefügt, in unserem Bild.
Folgender Text soll sich schick ins Bild einfügen oder in 3-D vielleicht in Schriftfarbe gold hervorheben:
Mit ganzem Herzen für Sie da!
Ihr Online -Juwelier mit Herz
Siehe auch unser altes Bild mit Text, im Shop, wie es nicht aussehen sollte: www.villamondlicht.de

```html
<!DOCTYPE html>
<html lang="de">
<head>
<meta charset="utf-8">
<title>Villa Mondlicht – Ihr Online-Juwelier mit Herz</title>
<link rel="stylesheet" href="https://fonts.googleapis.com/css2?family=Cabin:wght@400;600&family=Raleway:wght@400&family=Dancing+Script:wght@700&family=Handlee&display=swap">
<style>
  :root {
    --red: #c8101e;
    --text: #555555;
    --dark: #222222;
    --nav: #5e5e5e;
    --field: #eeeeee;
    --white: #ffffff;
    --silk-light: #f1eeec;
    --silk-mid: #d9d3cf;
    --gold: #d9a64a;
    --seal: #e4e4e4;
  }
  * { box-sizing: border-box; margin: 0; padding: 0; }
  html, body { width: 1200px; height: 1047px; overflow: hidden; background: var(--white); }
  body { position: relative; font-family: "Cabin", sans-serif; color: var(--text); }
  .abs { position: absolute; }

  .top-links { top: 12px; right: 213px; display: flex; gap: 15px; font-size: 10px; color: var(--dark); }
  .top-links .active { color: var(--red); }

  .brand { left: 214px; top: 40px; width: 120px; display: flex; align-items: center; gap: 6px; }
  .brand-dot { width: 12px; height: 12px; border-radius: 50%; background: var(--red); flex: none; }
  .brand-name { font-size: 17px; font-weight: 600; color: var(--red); line-height: 1.1; }

  .search-label { left: 413px; top: 64px; font-size: 13px; color: var(--dark); display: flex; align-items: center; gap: 7px; }
  .search-field { left: 413px; top: 87px; width: 334px; height: 31px; background: var(--field); font-size: 11px; color: var(--red); padding: 8px 20px; }
  .search-field svg { position: absolute; right: 12px; top: 6px; }
  .cart { left: 792px; top: 87px; width: 195px; height: 32px; background: var(--field); font-size: 11px; color: var(--red); padding: 9px 19px; }
  .cart svg { position: absolute; right: 16px; top: 7px; }

  .nav { left: 0; top: 146px; width: 1200px; height: 35px; background: var(--nav); }
  .nav ul { list-style: none; position: absolute; left: 311px; top: 9px; display: flex; gap: 30px; font-family: "Raleway", sans-serif; font-size: 13px; color: var(--white); text-transform: uppercase; letter-spacing: 0.1px; }

  .hero { left: 0; top: 181px; width: 1200px; height: 304px;
    background: radial-gradient(ellipse at 80% 45%, #f0d9a6 0%, rgba(240,217,166,0) 30%),
                linear-gradient(160deg, var(--silk-light) 0%, var(--silk-mid) 45%, #efe7df 70%, var(--silk-mid) 100%); }
  .hero-title { left: 232px; top: 286px; font-family: "Dancing Script", cursive; font-size: 41px; color: var(--red); transform: rotate(-4deg); transform-origin: left bottom; white-space: nowrap; }
  .hero-sub { left: 290px; top: 338px; font-family: "Cabin", sans-serif; font-size: 27px; color: var(--dark); transform: rotate(-2deg); transform-origin: left bottom; white-space: nowrap; }
  .hero-shade { left: 0; top: 485px; width: 1200px; height: 22px; background: linear-gradient(#c9c9c9, rgba(255,255,255,0)); }

  .store-line { left: 213px; top: 597px; font-size: 15px; }
  .store-line small { font-size: 12px; }
  .store-banner { left: 213px; top: 633px; width: 487px; height: 164px; background: linear-gradient(90deg, #2a2826 0%, #4a4642 55%, #c4662a 75%, #3c3936 100%); box-shadow: 0 0 3px rgba(0,0,0,0.4); }
  .store-name { left: 226px; top: 640px; font-family: "Cabin", sans-serif; font-size: 38px; color: var(--gold); letter-spacing: 1px; }
  .store-dots { left: 593px; top: 777px; display: flex; gap: 8px; }
  .store-dots span { width: 7px; height: 7px; border-radius: 50%; background: var(--white); }
  .store-dots span:first-child { background: var(--red); }

  .seal { left: 746px; top: 520px; width: 70px; height: 70px; border-radius: 50%; background: var(--seal); }
  .divider { left: 733px; width: 254px; border-top: 3px dotted #d6d6d6; }
  .benefits { left: 736px; top: 620px; list-style: none; font-size: 13.5px; color: var(--red); }
  .benefits li { display: flex; align-items: center; gap: 7px; height: 31.5px; }

  .welcome { left: 213px; top: 846px; font-family: "Handlee", cursive; font-size: 21px; font-weight: 400; color: var(--text); white-space: nowrap; }
  .welcome span { color: var(--red); }
  .lead { left: 213px; top: 893px; font-size: 15px; font-weight: 600; }
  .copy { left: 213px; top: 931px; width: 480px; font-size: 13.5px; line-height: 19.5px; white-space: nowrap; }
  .copy a { color: var(--text); }
</style>
</head>
<body>
  <nav class="top-links abs">
    <span class="active">Startseite</span><span>Anmelden</span><span>Mein Konto</span><span>Newsletter abonnieren</span><span>Kontakt</span>
  </nav>

  <div class="brand abs"><span class="brand-dot"></span><span class="brand-name">Villa Mondlicht</span></div>

  <div class="search-label abs">Nach welchem Artikel suchen Sie?
    <svg width="10" height="6" viewBox="0 0 10 6"><path d="M0 0h10L5 6z" fill="#c8101e"/></svg>
  </div>
  <div class="search-field abs">Suchen nach
    <svg width="22" height="19" viewBox="0 0 22 19"><path d="M11 19 1.5 9.5A5.5 5.5 0 0 1 11 3a5.5 5.5 0 0 1 9.5 6.5z" fill="#c8101e"/><circle cx="10.5" cy="8.5" r="2.5" fill="none" stroke="#fff" stroke-width="1.4"/><path d="M12.3 10.3 14 12" stroke="#fff" stroke-width="1.4"/></svg>
  </div>
  <div class="cart abs">Ihr Warenkorb ist leer.
    <svg width="16" height="19" viewBox="0 0 16 19"><rect x="0" y="5" width="16" height="14" rx="1" fill="#c8101e"/><path d="M4.5 5V3.5a3.5 3.5 0 0 1 7 0V5" fill="none" stroke="#c8101e" stroke-width="1.6"/><path d="M8 15 5 12a1.7 1.7 0 0 1 3-2 1.7 1.7 0 0 1 3 2z" fill="#fff"/></svg>
  </div>

  <div class="nav abs">
    <ul><li>Kreuz-Anhänger</li><li>Anhänger/Versch.</li><li>Foto-Medaillons</li><li>Ohrschmuck</li><li>Accessoires</li></ul>
  </div>

  <div class="hero abs" role="img" aria-label="Foto: goldener Herzanhänger an feiner Kette auf weißer Seide"></div>
  <div class="hero-title abs">Mit ganzem Herzen für Sie da!</div>
  <div class="hero-sub abs">Ihr Online -Juwelier mit Herz</div>
  <div class="hero-shade abs"></div>

  <p class="store-line abs">Besuchen Sie auch unseren AURELIQ-Schmuck Store: <small>hier</small></p>
  <div class="store-banner abs" role="img" aria-label="Foto: Goldschmiede-Tiegel mit Flamme in der Werkstatt, Hinweis auf Herstellung in Deutschland"></div>
  <div class="store-name abs">AURELIQ</div>
  <div class="store-dots abs"><span></span><span></span><span></span><span></span><span></span><span></span></div>

  <div class="seal abs" role="img" aria-label="Platz für ein Gütesiegel"></div>
  <div class="divider abs" style="top:598px"></div>

  <ul class="benefits abs">
    <li><svg width="19" height="17" viewBox="0 0 19 17"><path d="M9.5 17 1.4 8.6A4.8 4.8 0 0 1 9.5 2.6a4.8 4.8 0 0 1 8.1 6z" fill="#f2a0a8" stroke="#e04050"/></svg>Versand innerhalb von 24 Stunden</li>
    <li><svg width="19" height="17" viewBox="0 0 19 17"><path d="M9.5 17 1.4 8.6A4.8 4.8 0 0 1 9.5 2.6a4.8 4.8 0 0 1 8.1 6z" fill="#f2a0a8" stroke="#e04050"/></svg>schneller, persönlicher Service</li>
    <li><svg width="19" height="17" viewBox="0 0 19 17"><path d="M9.5 17 1.4 8.6A4.8 4.8 0 0 1 9.5 2.6a4.8 4.8 0 0 1 8.1 6z" fill="#f2a0a8" stroke="#e04050"/></svg>Kundenzufriedenheit an erster Stelle</li>
    <li><svg width="19" height="17" viewBox="0 0 19 17"><path d="M9.5 17 1.4 8.6A4.8 4.8 0 0 1 9.5 2.6a4.8 4.8 0 0 1 8.1 6z" fill="#f2a0a8" stroke="#e04050"/></svg>sichere Zahlungsmethoden</li>
  </ul>
  <div class="divider abs" style="top:755px"></div>

  <h1 class="welcome abs">Herzlich Willkommen im <span>VillaMondlicht.de</span> Schmuck-Shop</h1>
  <h2 class="lead abs">Ihr Online-Juwelier mit Herz</h2>
  <p class="copy abs"><a href="#">Hier finden Sie Schmuck-Ideen mit Herz / Made in Germany</a><br>Schmuck und Schmuck-Accessoires für Valentinstag, Muttertag,<br>Hochzeit, Verlobung und Hochzeitstag, für die Taufe, die Konfirmation,<br>die Kommunion.<br>Oder einfach ein besonderes Geschenk für einen besonderen Menschen.</p>
</body>
</html>
```